Business Card Revision

Need to redesign my business cards for a new professional look. We are a courier company. You can go to www.qvroutefast.com to see what we do. The trucks have an old company name (Nimble) on them but that is the company we are just now
changing the name.

Target Market(s)

Potential clients. We service the automotive, plumbing, printing, air freight industries as well as many others.

Industry/Entity Type

Business

Contact Information for Business Card

QVrushline
20583 Palmer Fenwick Parkway
Cincinnati, Oh 45317

Howard T. Lassiter
President

howie@qvroutefast.com

Main: (513) 555-0147

```html
<!DOCTYPE html>
<html lang="en">
<head>
<meta charset="utf-8">
<title>QV Routefast Business Card</title>
<link href="https://fonts.googleapis.com/css2?family=Open+Sans:wght@400;600;700&display=swap" rel="stylesheet">
<style>
  :root {
    --backdrop: #3b3431;
    --card: #1b1b1c;
    --brand-blue: #1f86d4;
    --brand-green: #3cb548;
    --text-light: #e6e6e6;
    --divider: #6b6b6b;
  }
  * { margin: 0; padding: 0; box-sizing: border-box; }
  html, body {
    width: 1200px;
    height: 814px;
    overflow: hidden;
    background: var(--backdrop);
    font-family: "Open Sans", Arial, sans-serif;
  }
  .stage {
    width: 1200px;
    height: 814px;
    display: flex;
    align-items: center;
    justify-content: center;
    gap: 60px;
  }
  .card {
    width: 540px;
    height: 309px;
    background: var(--card);
    position: relative;
    box-shadow: 0 10px 30px rgba(0,0,0,0.45);
  }
  .brand-name {
    font-weight: 700;
    color: var(--brand-blue);
    letter-spacing: 2px;
    white-space: nowrap;
  }
  /* Front side */
  .card-front {
    display: flex;
    flex-direction: column;
    align-items: center;
    justify-content: center;
  }
  .card-front .brand-name {
    font-size: 40px;
    margin-bottom: 34px;
  }
  .website {
    color: var(--text-light);
    font-size: 15px;
    letter-spacing: 3px;
  }
  /* Back side */
  .card-back .brand-name {
    position: absolute;
    top: 62px;
    left: 0;
    right: 0;
    text-align: center;
    font-size: 38px;
  }
  .details {
    position: absolute;
    top: 160px;
    left: 0;
    right: 0;
    display: flex;
    justify-content: center;
  }
  .person {
    text-align: right;
    padding-right: 18px;
    border-right: 1px solid var(--divider);
  }
  .person-name {
    color: var(--brand-blue);
    font-size: 18px;
    line-height: 1.2;
  }
  .person-title {
    color: var(--brand-green);
    font-size: 14px;
    line-height: 1.3;
  }
  .person-email {
    color: var(--text-light);
    font-size: 14px;
    margin-top: 6px;
  }
  .company {
    padding-left: 18px;
    color: var(--text-light);
    font-size: 14px;
    line-height: 1.45;
  }
  .phone {
    display: flex;
    align-items: center;
    gap: 6px;
  }
  .phone-icon {
    width: 12px;
    height: 12px;
    fill: var(--brand-blue);
  }
</style>
</head>
<body>
  <main class="stage">
    <section class="card card-front">
      <div class="brand-name">QV ROUTEFAST</div>
      <div class="website">www.qvroutefast.com</div>
    </section>

    <section class="card card-back">
      <div class="brand-name">QV ROUTEFAST</div>
      <div class="details">
        <div class="person">
          <div class="person-name">Howard T. Lassiter</div>
          <div class="person-title">President</div>
          <div class="person-email">howie@qvroutefast.com</div>
        </div>
        <div class="company">
          <div>QVrushline</div>
          <div>20583 Palmer Fenwick Parkway</div>
          <div>Cincinnati, Oh 45317</div>
          <div class="phone">
            <svg class="phone-icon" viewBox="0 0 24 24" aria-hidden="true">
              <path d="M6.6 10.8a15.1 15.1 0 0 0 6.6 6.6l2.2-2.2a1 1 0 0 1 1-.25 11.4 11.4 0 0 0 3.6.6 1 1 0 0 1 1 1V20a1 1 0 0 1-1 1A17 17 0 0 1 3 4a1 1 0 0 1 1-1h3.5a1 1 0 0 1 1 1c0 1.25.2 2.45.6 3.6a1 1 0 0 1-.25 1z"/>
            </svg>
            <span>(513) 555-0147</span>
          </div>
        </div>
      </div>
    </section>
  </main>
</body>
</html>
```